Training Course Info Brochure

Hi there, I'm looking for a design for A4 Flyer (2-3 pages) on our new Course - Infection Control. I have included a previous brochure on our courses so the designed can see the look and feel we are looking for.

As this is about Infection Control, I would also like to see some RED in the design or wording.

The brochure will need to include quite a few industry/ government logos as well and graphics are important. I have included some (Health Care Industry workers) and am also open to other graphics.

Thanks for considering!

Target Market(s)

The Health profession and students wanting to work in the health field

Industry/Entity Type

Health Care

Font styles to use
Sans Serif

Colors
3277b5
f78f20
ffffff
ec1f27

Requirements
Must have
• Similar feel to the brochure I have included in this brief.

SOME RED lettering as we are teaching Infection Control during the COVID19 pandemic
Nice to have
• Lovely design with quite a few photos graphics

Company details:

Carrow Academy of Learning
RTO 73648
FREECALL : 1800 437 982
www.carrowlearning.edu.au
info@carrowlearning.edu.au

```html
<!DOCTYPE html>
<html lang="en">
<head>
<meta charset="utf-8">
<title>Infection Control Course Brochure</title>
<link href="https://fonts.googleapis.com/css2?family=Roboto+Condensed:wght@700&family=Montserrat:wght@400;600;700&display=swap" rel="stylesheet">
<style>
:root{
  --navy:#0f4a87;
  --orange:#cf8f2c;
  --bullet:#f08a1c;
  --red:#e01f26;
  --ink:#2a2a2a;
  --paper:#ffffff;
  --backdrop:#e7e7e7;
  --photo-dark:#6b6b6b;
  --photo-light:#cfcfcf;
}
*{margin:0;padding:0;box-sizing:border-box}
html,body{width:1200px;height:907px;overflow:hidden;background:var(--backdrop)}
body{position:relative;font-family:"Montserrat",Arial,sans-serif;color:var(--ink)}
.page{position:absolute;top:58px;height:790px;background:var(--paper);overflow:hidden}
.page--left{left:80px;width:518px}
.page--right{left:600px;width:542px}
.abs{position:absolute}
.photo{position:absolute}
.photo--carer{left:0;top:0;width:518px;height:322px;background:linear-gradient(120deg,#8a8a8a,#d6d6d6 55%,#9a9a9a)}
.photo-rule{left:0;top:322px;width:518px;height:6px;background:var(--orange)}
.heading{font-family:"Roboto Condensed",Arial,sans-serif;font-weight:700;text-transform:uppercase;letter-spacing:.2px}
.heading--dark{color:#222;font-size:17px}
.heading--light{color:#fff;font-size:16px}
.rule{height:1px;background:#555}
.rule--light{background:#fff}
.lead-red{color:var(--red);font-weight:700;font-size:8.8px;line-height:1.4}
.body-copy{font-size:8.1px;line-height:1.45}
.body-copy p{margin-bottom:9px}
.format-box{left:270px;top:220px;width:230px;height:382px;background:var(--navy);color:#fff;padding:14px 12px}
.format-box .rule{margin:6px 0 10px}
.sub-orange{color:var(--bullet);font-weight:700;font-size:8.6px;line-height:1.35;margin-bottom:14px}
.format-box .body-copy{color:#fff}
.band-line{height:4px;background:var(--navy)}
.band{height:36px;background:var(--orange)}
.page-num{width:30px;height:30px;border:2px solid var(--navy);background:#fff;color:var(--navy);font-weight:700;font-size:14px;display:flex;align-items:center;justify-content:center}
.skills-panel{left:7px;top:10px;width:535px;height:288px;background:var(--navy);color:#fff}
.photo--gloves{left:297px;top:20px;width:245px;height:210px;background:radial-gradient(circle at 50% 50%,#f2f2f2,#a9a9a9)}
.list{list-style:none;font-size:8px;line-height:1.25}
.list li{position:relative;padding-left:14px;margin-bottom:3.2px}
.list li::before{content:"";position:absolute;left:2px;top:3px;width:5px;height:5px;border-radius:50%;background:var(--bullet)}
.list--white{color:#fff}
.list--sq li::before{border-radius:0;width:4px;height:4px;background:var(--navy)}
.list--dot li::before{background:var(--navy)}
.list--sm{font-size:6.8px}
.list--sm li{margin-bottom:3.6px}
.intro-strong{font-family:"Montserrat",Arial,sans-serif;font-weight:700;font-size:10.6px;color:#222}
.photo--nurse{left:8px;top:458px;width:197px;height:330px;background:linear-gradient(160deg,#9c9c9c,#e0e0e0 60%,#8e8e8e)}
.link{color:var(--red)}
</style>
</head>
<body>

<section class="page page--left">
  <div class="photo photo--carer" role="img" aria-label="Black and white photo of a young nurse smiling with an elderly woman holding a cup"></div>
  <div class="abs photo-rule"></div>

  <h2 class="abs heading heading--dark" style="left:17px;top:350px">About this course</h2>
  <div class="abs rule" style="left:17px;top:374px;width:232px"></div>
  <p class="abs lead-red" style="left:17px;top:386px;width:232px">Protect yourself and others in the community from infectious diseases</p>

  <div class="abs body-copy" style="left:17px;top:428px;width:242px">
    <p>There is not better time than now, to formally Upskill yourself and your team with a Nationally Accredited unit of Competency in Infection Control prevention including the latest COVID19 infection control protocols (Department of Health). Fast track your skills with Carrow's Accredited Infection Control Skill set to get you job ready or enhance your current workplace skills.</p>
    <p>The COVID19 pandemic has highlighted the important of building the capacity and understanding of the workforce to practice safe infection control procedures.</p>
    <p>This skill set will provide you with the skills and knowledge to assist inprotecting yourself and others in the community from infectious diseases.</p>
    <p>You will understand how infections are spread, ways of preventing the spread of infection and how to protect yourselfand others from infection.</p>
    <p>The skill set is becoming increasingly important for all Health Care Workers – and all workers are encouraged to upskill themselves today, whether you are becoming Job Ready or for your professional development in Industry.</p>
  </div>

  <div class="abs format-box">
    <h2 class="heading heading--light">Course format-</h2>
    <div class="rule rule--light"></div>
    <p class="sub-orange">Online with face-to-face tutorial<br>(in person or via Meetly)</p>
    <div class="body-copy">
      <p>Our course is delivered to you online which allows you to undertaken study at your own pace. It is recommended completion occurs within a month.</p>
      <p>you have completed the Online Component of your course, you are invited into a Practical Lab Session via face to face learning, to practice skills and undertake a workplace simulated activity.</p>
      <p>Regional locations may be fulfilled by Meetly technology and Carrow may also conduct on-site visits as required. Carrow also travel to regional locations throughout the year. Group training sessions are also available for corporates and workplaces.</p>
    </div>
    <p class="sub-orange" style="margin-top:14px;margin-bottom:10px">Mentor Support and Practical Sessions</p>
    <div class="body-copy">
      <p>Students are welcomed to the course by a short induction by your Tutor/Mentor to start you on your way with confidence! All of Carrow's student resources, learner materials, videos are contained in Carrow's easy to use LMS and learning is provided online at your convenience.</p>
    </div>
  </div>

  <p class="abs lead-red" style="left:270px;top:623px">Industry Recognised</p>
  <div class="abs body-copy" style="left:270px;top:650px;width:234px">
    <p>Carrow's unique program in Infection Control is supported by leading Industry bodies, and includes certification by the Department of Health, and other leading Health bodies in Australia. Our Unit of competency is Australian Recognised and Accredited.</p>
  </div>

  <div class="abs band-line" style="left:75px;top:748px;width:443px"></div>
  <div class="abs band" style="left:75px;top:752px;width:443px"></div>
  <div class="abs page-num" style="left:16px;top:746px">2</div>
</section>

<section class="page page--right">
  <div class="abs skills-panel">
    <h2 class="abs heading heading--light" style="left:13px;top:14px;font-size:17px">Gain these skills :</h2>
    <div class="abs rule rule--light" style="left:0;top:40px;width:272px"></div>
    <ul class="abs list list--white" style="left:13px;top:52px;width:275px">
      <li>Gain Industry Certification in Hand Hygiene</li>
      <li>Gain Industry Certification in COVID19 Infection Control</li>
      <li>Gain Industry Certification in Cleaning, Disinfection and Sterilisation</li>
      <li>Using personal protective equipment safely (practical session with complimentary PPE samples)</li>
      <li>Understanding the chain of infection</li>
      <li>Identify infection hazards and assess risks</li>
      <li>How to prevent the spread and transmission of infection</li>
      <li>Maintaining a clean work environment</li>
    </ul>
    <h2 class="abs heading heading--light" style="left:13px;top:196px;font-size:17px">Who this course is ideal for :</h2>
    <div class="abs rule rule--light" style="left:0;top:222px;width:272px"></div>
    <p class="abs body-copy" style="left:13px;top:234px;width:270px;color:#fff;font-size:8px">The skill set course is most suitable for anyone working the healthcare sector, or those looking to enter employment in the health fields.</p>
  </div>
  <div class="photo photo--gloves" role="img" aria-label="Two gloved hands forming a heart shape"></div>

  <p class="abs intro-strong" style="left:18px;top:312px">This training is for care workers across all health care settings, including:</p>
  <ul class="abs list list--dot" style="left:14px;top:338px;width:500px">
    <li>Hospitals and Primary care</li>
    <li>Medical practices, allied health, GP and specialist clinics</li>
    <li>Aged care (both in residential aged care facilities or with visiting carers at home, including cleaners and cooks)</li>
    <li>Disability (both in residential/shared care facilities or part-time carers in people's homes, including cleaners and cooks)</li>
    <li>Allied health, Aboriginal Community Controlled Health Services and Pharmacies</li>
    <li>Dental practices, including dentists, nurses, cleaners and receptionists</li>
  </ul>

  <div class="photo photo--nurse" role="img" aria-label="Black and white photo of a nurse washing her hands at a clinic sink"></div>
  <h2 class="abs heading heading--dark" style="left:216px;top:460px">Job opportunities and study pathways</h2>
  <div class="abs rule" style="left:205px;top:484px;width:320px"></div>
  <div class="abs body-copy" style="left:216px;top:497px;width:300px">
    <p>This course does not lead to a specific job outcome but will be helpful if you are, or would like to work in any of the areas described above. Our training course is designed to make students Job Ready or to enhance their job role.</p>
    <p>The Units of Competency is a recognised Unit that can be used as a Credit Transfer in Qualifications such as:</p>
  </div>
  <ul class="abs list list--sq list--sm" style="left:216px;top:590px;width:310px">
    <li>Certificate III Business Administration (Medical)</li>
    <li>Cert III and IV Health Administration</li>
    <li>Cert III in Individual Support (Aging, disability, home and community)</li>
    <li>Cert III in Allied Health Assistance</li>
    <li>Cert III/IV Dental Assisting</li>
    <li>Certificate III in Aboriginal and/or Torres Strait Islander Primary Health Care</li>
    <li>Cert II/III Community Services</li>
    <li>Certificate III in Cleaning Operations</li>
    <li>Cert II and III Health Support Services</li>
  </ul>
  <p class="abs body-copy" style="left:216px;top:700px;width:310px;font-weight:600">More Qualifications that include this Unit of Competency can be found at <span class="link">https://trainingregister.edu.au/Details/HLTINF001</span></p>

  <div class="abs band-line" style="left:0;top:748px;width:490px"></div>
  <div class="abs band" style="left:0;top:752px;width:490px"></div>
  <div class="abs page-num" style="left:490px;top:736px">3</div>
</section>

</body>
</html>
```